New business card design needed for Trucking/Staffing company!

I am looking for a business card design. The business name is Keystone Haul Partners, LLC. This company is a staffing company for commercial drivers/truck drivers. Most of our customers are trucking/supply companies. Our colors are blue/black/white/grey. The info I have on my current business cards is
-Spot for a name
-2 lines for an address
-3 lines for Office, cell, and fax
-email
-website(currently on backside of card with logo but can go anywhere)
Updates

Project Deadline Extended
Reason: Open to more designs

Target Market(s)

Trucking companies, building supply companies

Industry/Entity Type

Business

Contact Information for Business Card

Edgy but professional

Font styles to use
Other font styles liked:
• Open to suggestions

Colors
0555a3
000000
ffffff
9d9d9d

Requirements
Must have
• Must have the logo incorporated

```html
<!DOCTYPE html>
<html lang="en">
<head>
<meta charset="utf-8">
<title>Keystone Haul Partners – Business Card</title>
<link href="https://fonts.googleapis.com/css2?family=Open+Sans:wght@400;600;700&display=swap" rel="stylesheet">
<style>
  :root {
    --brand-blue: #0555a3;
    --deep-blue: #1f2f8f;
    --ink: #000000;
    --charcoal: #3a3a3c;
    --grey: #9d9d9d;
    --text-grey: #4a4a4a;
    --paper: #ffffff;
    --backdrop: #e6e6e6;
  }
  * { margin: 0; padding: 0; box-sizing: border-box; }
  html, body { width: 1200px; height: 843px; overflow: hidden; }
  body {
    background: var(--backdrop);
    font-family: "Open Sans", Arial, sans-serif;
    position: relative;
  }
  .card {
    position: absolute;
    top: 273px;
    width: 520px;
    height: 297px;
    border-radius: 3px;
    box-shadow: 0 6px 18px rgba(0,0,0,0.18);
    overflow: hidden;
  }
  /* Back side */
  .card-back {
    left: 50px;
    background: linear-gradient(100deg, var(--charcoal) 0%, var(--charcoal) 28%, var(--deep-blue) 62%, var(--brand-blue) 100%);
  }
  .card-back .brand-art {
    position: absolute;
    inset: 0;
  }
  .card-back .brand-block {
    position: absolute;
    right: 34px;
    bottom: 46px;
    text-align: right;
    color: var(--paper);
  }
  .card-back .brand-name {
    font-weight: 700;
    font-size: 24px;
    letter-spacing: 1px;
    text-transform: uppercase;
  }
  .card-back .brand-web {
    margin-top: 4px;
    font-size: 15px;
    letter-spacing: 2px;
    color: #dfe3f2;
  }
  /* Front side */
  .card-front {
    left: 630px;
    background: linear-gradient(135deg, var(--paper) 55%, #ededed 100%);
    padding: 30px 34px;
    color: var(--text-grey);
  }
  .person-name {
    color: var(--deep-blue);
    font-weight: 700;
    font-size: 19px;
    line-height: 1.1;
  }
  .person-title {
    font-size: 13px;
    margin-top: 2px;
  }
  .address {
    margin-top: 34px;
    font-size: 13px;
    line-height: 1.5;
  }
  .contact-list {
    list-style: none;
    margin-top: 6px;
    font-size: 13px;
  }
  .contact-list li {
    display: flex;
    align-items: center;
    gap: 9px;
    height: 21px;
  }
  .contact-list svg {
    width: 12px;
    height: 12px;
    fill: var(--deep-blue);
    flex: none;
  }
  .card-front .brand-mark {
    position: absolute;
    right: 32px;
    bottom: 34px;
    color: var(--deep-blue);
    font-weight: 700;
    font-size: 18px;
    letter-spacing: 0.5px;
    text-transform: uppercase;
  }
</style>
</head>
<body>

<section class="card card-back" aria-label="Card back">
  <div class="brand-art" role="img" aria-label="Large truck emblem decoration in grey and blue"></div>
  <div class="brand-block">
    <div class="brand-name">Keystone Haul Partners</div>
    <div class="brand-web">www.keystonehaul.com</div>
  </div>
</section>

<section class="card card-front" aria-label="Card front">
  <div class="person-name">Daniel Reyes</div>
  <div class="person-title">CEO/Founder</div>

  <address class="address" style="font-style:normal">
    4120 Larkspur Drive<br>
    Fairbanks, Alaska 99701
  </address>

  <ul class="contact-list">
    <li>
      <svg viewBox="0 0 24 24" aria-hidden="true"><path d="M6.6 10.8a15.1 15.1 0 0 0 6.6 6.6l2.2-2.2c.3-.3.7-.4 1-.2 1.1.4 2.3.6 3.6.6.6 0 1 .4 1 1V20c0 .6-.4 1-1 1A17 17 0 0 1 3 4c0-.6.4-1 1-1h3.5c.6 0 1 .4 1 1 0 1.3.2 2.5.6 3.6.1.3 0 .7-.2 1z"/></svg>
      <span class="contact-office">555 210 4418</span>
    </li>
    <li>
      <svg viewBox="0 0 24 24" aria-hidden="true"><path d="M7 1h10a2 2 0 0 1 2 2v18a2 2 0 0 1-2 2H7a2 2 0 0 1-2-2V3a2 2 0 0 1 2-2zm0 3v14h10V4zm5 15.5a1.2 1.2 0 1 0 0 2.4 1.2 1.2 0 0 0 0-2.4z"/></svg>
      <span class="contact-cell">555 372 9051</span>
    </li>
    <li>
      <svg viewBox="0 0 24 24" aria-hidden="true"><path d="M6 2h10l2 2v5H6zM3 10h18a2 2 0 0 1 2 2v7H1v-7a2 2 0 0 1 2-2zm3 10h12v2H6z"/></svg>
      <span class="contact-fax">555 604 7723</span>
    </li>
    <li>
      <svg viewBox="0 0 24 24" aria-hidden="true"><path d="M2 5h20v14H2zm2 2v.5l8 5 8-5V7l-8 5z"/></svg>
      <span class="contact-email">hello@keystonehaul.com</span>
    </li>
    <li>
      <svg viewBox="0 0 24 24" aria-hidden="true"><circle cx="12" cy="12" r="10"/></svg>
      <span class="contact-web">www.keystonehaul.com</span>
    </li>
  </ul>

  <div class="brand-mark">Keystone Haul Partners</div>
</section>

</body>
</html>
```